Northvale Coaching Company requires banner design

I need 3 large banners designed. i will be using these for advertising and also a condensed version as the header on a splash pages.

I have attached the wording and also the photo's that i'd like used in each design.
Note: i've just placed the wording randomly, you'll have to place it where it makes the most sense for the message and the design.

I want something with bright colors that pops.

Reason: I'd like to give the most recent designers time to submit quality work.

```html
<!DOCTYPE html>
<html lang="en">
<head>
<meta charset="utf-8">
<title>Northvale Coaching Company – Free Info Banner</title>
<link rel="stylesheet" href="https://fonts.googleapis.com/css2?family=Oswald:wght@300;400;600;700&family=Roboto+Condensed:wght@400;700&display=swap">
<style>
  :root {
    --bg: #ffffff;
    --ink: #111111;
    --red: #e3161b;
    --band-light: #fff46a;
    --band-mid: #f4de1a;
    --band-deep: #e8c60c;
    --badge: #fbf07a;
    --stage-pink: #e8359a;
    --stage-purple: #7b3fc4;
    --stage-blue: #3a6fd8;
    --stage-dark: #3b1d4a;
  }
  * { margin: 0; padding: 0; box-sizing: border-box; }
  html, body { width: 1200px; height: 360px; overflow: hidden; background: var(--bg); }
  .banner {
    position: relative;
    width: 1200px;
    height: 360px;
    overflow: hidden;
    background: var(--bg);
    font-family: "Roboto Condensed", "Arial Narrow", sans-serif;
    color: var(--ink);
  }
  .hero-photo {
    position: absolute;
    left: 0; top: 0;
    width: 640px; height: 360px;
  }
  .hero-photo svg { display: block; width: 100%; height: 100%; }

  .offer {
    position: absolute;
    left: 560px; width: 480px;
    top: 10px;
    text-align: center;
    font-family: "Oswald", sans-serif;
    font-weight: 700;
    font-size: 47px;
    line-height: 1;
    letter-spacing: 0.5px;
    color: var(--red);
  }
  .questions {
    position: absolute;
    left: 360px; width: 880px;
    top: 74px;
    text-align: center;
    list-style: none;
    font-family: "Oswald", sans-serif;
    font-weight: 600;
    font-size: 25px;
    line-height: 36px;
    color: var(--ink);
  }
  .promise {
    position: absolute;
    left: 470px; width: 640px;
    top: 198px;
    text-align: center;
    font-family: "Roboto Condensed", sans-serif;
    font-weight: 400;
    font-size: 23px;
    line-height: 29px;
    color: var(--ink);
  }
  .benefits {
    position: absolute;
    left: 20px; top: 290px;
    width: 1180px; height: 40px;
    background: linear-gradient(90deg, rgba(244,222,26,0) 0%, var(--band-mid) 5%, var(--band-light) 50%, var(--band-deep) 100%);
  }
  .benefit {
    position: absolute;
    top: 8px;
    font-size: 19px;
    line-height: 24px;
    white-space: nowrap;
    color: var(--ink);
  }
  .benefit--home { left: 80px; }
  .benefit--mlm { left: 218px; }
  .benefit--calls { left: 330px; }
  .benefit--formula { left: 515px; }
  .benefit--opportunity { left: 775px; }
  .badge {
    position: absolute;
    left: 945px; top: 276px;
    width: 255px; height: 60px;
    background: linear-gradient(180deg, var(--badge), var(--band-mid));
    text-align: center;
    font-family: "Oswald", sans-serif;
    font-weight: 400;
    font-size: 38px;
    line-height: 58px;
    color: var(--ink);
  }
</style>
</head>
<body>
<main class="banner">
  <div class="hero-photo" role="img" aria-label="Photo of the two coaches, a smiling man and woman, in front of a colourful pink, purple and blue stage-light backdrop">
    <svg viewBox="0 0 640 360" preserveAspectRatio="none">
      <defs>
        <radialGradient id="stageGlow" cx="0.3" cy="0.35" r="0.7">
          <stop offset="0" stop-color="var(--stage-pink)"/>
          <stop offset="0.45" stop-color="var(--stage-purple)"/>
          <stop offset="0.8" stop-color="var(--stage-blue)"/>
          <stop offset="1" stop-color="var(--stage-dark)"/>
        </radialGradient>
        <linearGradient id="fadeOut" x1="0" x2="1" y1="0" y2="0">
          <stop offset="0" stop-color="#fff" stop-opacity="1"/>
          <stop offset="0.66" stop-color="#fff" stop-opacity="1"/>
          <stop offset="0.97" stop-color="#fff" stop-opacity="0"/>
        </linearGradient>
        <mask id="fadeMask">
          <rect width="640" height="360" fill="url(#fadeOut)"/>
        </mask>
      </defs>
      <rect width="640" height="360" fill="url(#stageGlow)" mask="url(#fadeMask)"/>
    </svg>
  </div>

  <h1 class="offer">FREE INFO CLICK HERE</h1>

  <ul class="questions">
    <li>Passionate about Personal Development / Leadership Development?</li>
    <li>Looking to align yourself with an opportunity of substance?</li>
    <li>Ready to be challenged &amp; encouraged to reach new level’s of success?</li>
  </ul>

  <p class="promise">“Let us show you how we’ve taught others like you to make a<br>quantum leap in their personal results”</p>

  <div class="benefits">
    <span class="benefit benefit--home">Home Based</span>
    <span class="benefit benefit--mlm">- NOT MLM</span>
    <span class="benefit benefit--calls">- No Cold Calling</span>
    <span class="benefit benefit--formula">- Simple Success Formula</span>
    <span class="benefit benefit--opportunity">- Opportunity for</span>
  </div>
  <div class="badge">“Big Thinker”</div>
</main>
</body>
</html>
```